Rising Stewards Scheme. Brochure to Inform Target Audience.

Rising Steward Scheme:

4 Page Brochure
Aimed at Parents and Children (Age 11-16)
Programme Overview
Specific Focus on Bronze Award with Learning Objectives and Enabling Objectives from Content Document
Contact Area Needed
How to Book - Online through the Website
Should encourage people to want to join it or sign up

you can use stock rugby images if needed

Target Market(s)

children between ages 11-16 and parents, gatekeepers (schools, rugby clubs)

Industry/Entity Type

Education

Font styles to use
Serif
Sans Serif

Requirements
Must have
• the programme content, each award continent and bronze award learning objectives
• Colours should match existing work that has been created
• Get in touch: www.valemark-rss.com
• maris@valemark-rss.com
Nice to have
• graphics of kids playing rugby if possible from stock images

```html
<!DOCTYPE html>
<html lang="en">
<head>
<meta charset="utf-8">
<title>Rising Stewards Scheme – Brochure Spread</title>
<link rel="stylesheet" href="https://fonts.googleapis.com/css2?family=Open+Sans:wght@400;700;800&display=swap">
<style>
  :root {
    --backdrop: #d9d0ca;
    --paper: #f6f6f6;
    --paper-shade: #ebebeb;
    --green: #1d5a32;
    --green-dark: #154526;
    --gold: #f2b71c;
    --text: #4a4a4a;
    --photo-dark: #1c2a22;
    --photo-pitch: #3f7a35;
    --photo-crowd: #5a4f46;
  }
  * { box-sizing: border-box; margin: 0; padding: 0; }
  html, body {
    width: 1200px;
    height: 833px;
    overflow: hidden;
    background: var(--backdrop);
    font-family: "Open Sans", Arial, sans-serif;
  }
  .spread {
    position: absolute;
    left: 60px;
    top: 46px;
    width: 1080px;
    height: 740px;
    display: flex;
    box-shadow: 0 14px 30px rgba(0,0,0,.18);
  }
  .page {
    position: relative;
    width: 540px;
    height: 740px;
    overflow: hidden;
    background: var(--paper);
  }
  .page--left { background: linear-gradient(90deg, var(--paper) 80%, var(--paper-shade)); }
  .page--right { background: linear-gradient(90deg, var(--paper-shade), var(--paper) 18%); }

  .photo {
    position: absolute;
    top: 22px;
    left: 26px;
    right: 26px;
    height: 230px;
  }
  .photo--haka {
    background:
      linear-gradient(180deg, var(--photo-crowd) 0%, var(--photo-dark) 40%, var(--photo-dark) 70%, var(--photo-pitch) 100%);
  }
  .photo--match {
    height: 200px;
    background:
      linear-gradient(180deg, var(--photo-crowd) 0%, #2f3a2f 35%, var(--photo-pitch) 60%, #4d8a3c 100%);
  }
  .photo-curve {
    position: absolute;
    left: 0;
    width: 540px;
    height: 80px;
  }
  .page--left .photo-curve { top: 200px; }

  .content {
    position: absolute;
    left: 40px;
    right: 40px;
    color: var(--text);
  }
  .page--left .content { top: 290px; }
  .page--right .content { top: 248px; }

  .faq__question, .section__title {
    color: var(--green);
    font-weight: 800;
    font-size: 17px;
    line-height: 1.2;
    margin-bottom: 4px;
  }
  .faq__answer, .section__body {
    font-size: 10.5px;
    line-height: 1.45;
    margin-bottom: 18px;
  }
  .section__body + .section__body { margin-top: -10px; }

  .page-band {
    position: absolute;
    left: 0;
    bottom: 0;
    width: 540px;
    height: 140px;
  }
</style>
</head>
<body>
  <main class="spread">
    <section class="page page--left">
      <div class="photo photo--haka" role="img" aria-label="Rugby team in black kit performing a pre-match team ritual on the pitch"></div>
      <svg class="photo-curve" viewBox="0 0 540 80" preserveAspectRatio="none" aria-hidden="true">
        <path d="M0 80 L0 40 Q270 -10 540 20 L540 80 Z" fill="var(--paper)"/>
      </svg>

      <div class="content faq">
        <h2 class="faq__question">Will you provide lunch or snacks?</h2>
        <p class="faq__answer">Water will be provided to refill water bottles. However, we ask that children bring their own lunch.</p>

        <h2 class="faq__question">Who attends your Rising Stewards Scheme?</h2>
        <p class="faq__answer">Children of all abilities, some who have played rugby before and some who have never played. The programme is available to both boys and girls.</p>

        <h2 class="faq__question">What should my child wear?</h2>
        <p class="faq__answer">Activities will take place both indoor and outdoor; therefore, please ensure you bring appropriate rugby kit, including waterproofs and a change of kit, also trainers and boots.</p>

        <h2 class="faq__question">Will I meet a Valemark Mentor?</h2>
        <p class="faq__answer">Yes. Whilst on the programme you will have a chance to meet and learn from a Valemark Mentor.</p>
      </div>

      <svg class="page-band" viewBox="0 0 540 140" preserveAspectRatio="none" aria-hidden="true">
        <path d="M0 140 Q300 110 540 8 L540 140 Z" fill="var(--gold)"/>
        <path d="M0 140 Q310 118 540 16 L540 140 Z" fill="var(--green)"/>
      </svg>
    </section>

    <section class="page page--right">
      <div class="photo photo--match" role="img" aria-label="Rugby players in green and gold kits contesting the ball during a match"></div>

      <div class="content">
        <h2 class="section__title">Programme Overview</h2>
        <p class="section__body">The Valemark team have created a programme which enables each individual to maximise their learning potential so that you can be the best you can be. We provide a fun and healthy environment which is supported by highly motivated coaches which provide excellent individual care and attention. The programme is delivered over three Awards; Bronze, Silver and Gold.</p>

        <h2 class="section__title">Bronze Award</h2>
        <p class="section__body">The Bronze Award is focused on the 'Team' and is aimed at Children between the age of 11 and 13. During the Award you will improve your self-confidence and independence whilst having the opportunity to lead and inspire others.</p>
        <p class="section__body">We will encourage your natural skills and help you identify any areas that you may wish to develop in the future. Each day we will build your skills through both physical and mental challenges both on and off the pitch. The Award is delivered over 5 days. Days 1 and 2 are delivered at the Home of Rugby, Harrowmead and days 3 to 5 are delivered at Kestrel Vale RFC.</p>

        <h2 class="section__title">Silver Award</h2>
        <p class="section__body">On completion of the Bronze Award you are eligible to enrol on the Silver Award which is focused on the 'Individual'.</p>
      </div>

      <svg class="page-band" viewBox="0 0 540 140" preserveAspectRatio="none" aria-hidden="true">
        <path d="M0 8 Q240 30 540 30 L540 40 Q240 44 0 16 Z" fill="var(--gold)"/>
        <path d="M0 16 Q220 46 540 40 L540 52 Q260 70 0 140 Z" fill="var(--green)"/>
      </svg>
    </section>
  </main>
</body>
</html>
```